Modern e-Commerce Website for new tea company

We need a web design for a new company called "leaf meadows" based in the UK. We are operating in the food / retailing industry. We are an online retailer of organic Darjeeling Tea (Black and Green Tea) - our clients are end-customers within the UK.

We are looking for a coded wordpress webdesign for a landing page, a potential second page and an online shop.

Target Market(s)

End-customers of tea within the UK

Industry/Entity Type

E-Commerce

Coding

Coded - Design and coding required

Number of Pages Required

3 page

Font styles to use
Other font styles liked:
• Helvetica Neue

Requirements
Must have
• Design expectations:
• We are looking for a very professional looking website. A website that shows the type quality we put into preparing our tea every day. Overall theme of the website should be simplie and clean (white, green). But pictures of tea should be more colourful. Graphics like buttons, text, etc. should be simple, shouldn't stick out too much. Also, don't forget that this website is for people buying tea, so the design should make tea look more appetising.
• Websites that inspire us are:
• https://www.brovelle.co.uk/about-brovelle/brovelle-teas/darjeeling
• - nice colours, icons, graphics
• https://www.quenpo.com/
• - well designed, simple
• https://www.dulvo.com/
• - simple, clear sections for each point
• How we want each page to be designed
• 1) Landing Page (one-page)
• - sticky menu (header)
• - section 1: slider with pictures of our products
• - section 2: product overview with product pictures
• - section 3: advantages of our products
• - section 4: how our concept works
• - contact us
• - footer (twitter, fb, instagram, disclaimer)
• 2) Second page
• 3) Shop
• Our current site is: http://marquin.sitebarn.pw/wp/
Nice to have
• What to avoid
• We want this website to consist of soft colours, so we DON'T want colours that are too hard on the eyes and are "highlighter" like colours. We don't want this website to look too "cartoon like" or too "childish". We are going for a sophisticated, high class look.

```html
<!DOCTYPE html>
<html lang="en">
<head>
<meta charset="utf-8">
<title>Hillmist Teas – Organic Darjeeling Tea</title>
<link rel="stylesheet" href="https://fonts.googleapis.com/css2?family=Roboto+Slab:wght@400;500;700&family=Roboto:wght@400;500;700&family=Open+Sans:wght@400;600&family=Raleway:wght@400;500&display=swap">
<style>
:root{
  --rust:#b6482a;
  --teal:#3b5956;
  --ink:#222;
  --muted:#666;
  --mist:#ececec;
  --footer:#3c2e30;
  --gold:#dcc17d;
  --white:#fff;
}
*{box-sizing:border-box;margin:0;padding:0}
html,body{width:1200px;height:2773px;overflow:hidden}
body{position:relative;font-family:"Open Sans",Arial,sans-serif;color:var(--ink);background:var(--white)}
.abs{position:absolute}
section,footer{position:absolute;left:0;width:1200px}

/* hero */
.hero{top:0;height:597px;overflow:hidden}
.hero-photo{position:absolute;inset:0;background:
  linear-gradient(180deg,rgba(30,25,15,.55) 0%,rgba(60,45,25,.35) 45%,rgba(120,100,70,.45) 100%),
  radial-gradient(ellipse at 65% 10%,#c89a52 0%,#6d5a34 35%,#3a3a22 70%),#3c3a26}
.brand{position:absolute;left:98px;top:28px;width:220px;text-align:center;color:var(--white)}
.brand-mark{width:110px;height:110px;border-radius:50%;border:3px solid var(--white);margin:0 auto 14px}
.brand-name{font-family:"Roboto",Arial,sans-serif;font-weight:700;font-size:17px;letter-spacing:.3px}
.topbar{position:absolute;top:40px;right:88px;display:flex;gap:26px;align-items:center;color:var(--white);font-family:"Roboto",Arial,sans-serif;font-size:15px}
.topbar span{display:flex;align-items:center;gap:10px}
.ico-ring{width:34px;height:34px;border-radius:50%;background:rgba(255,255,255,.85);display:flex;align-items:center;justify-content:center}
.nav{position:absolute;top:112px;right:88px;display:flex;gap:32px;font-family:"Roboto",Arial,sans-serif;font-weight:500;font-size:15px;color:var(--white)}
.nav a{color:inherit;text-decoration:none;padding-bottom:10px}
.nav a.current{border-bottom:2px solid var(--white)}
.hero-title{position:absolute;left:98px;top:270px;font-family:"Roboto Slab",Georgia,serif;font-size:56px;font-weight:500;color:var(--white)}
.hero-sub{position:absolute;left:98px;top:370px;font-family:"Roboto",Arial,sans-serif;font-size:22px;line-height:40px;color:var(--white);font-weight:500}
.hero-arrows{position:absolute;left:98px;top:476px;display:flex;gap:12px}
.round-btn{width:40px;height:40px;border:2px solid var(--white);border-radius:50%;display:flex;align-items:center;justify-content:center}

/* products */
.teas{top:597px;height:411px;background:var(--white)}
.teas-photo{position:absolute;left:111px;top:62px;width:425px;height:278px;border-radius:50%;
  background:radial-gradient(ellipse at 45% 40%,#c27a2a 0%,#8a4a18 30%,rgba(60,40,25,.45) 55%,rgba(255,255,255,0) 70%)}
.teas-body{position:absolute;left:586px;top:48px;width:520px}
.sec-title{font-family:"Roboto Slab",Georgia,serif;font-weight:500;font-size:33px;color:var(--ink)}
.sec-title em{font-style:normal;color:var(--rust)}
.teas-lead{font-family:"Roboto",Arial,sans-serif;font-weight:500;font-size:18px;line-height:28px;margin-top:14px;width:460px}
.teas-copy{font-size:12px;line-height:22px;color:var(--muted);margin-top:18px;text-align:justify}
.btn{display:inline-block;background:var(--rust);color:var(--white);font-family:"Roboto",Arial,sans-serif;font-weight:500;font-size:14px;padding:11px 28px;border-radius:2px;margin-top:20px}

/* advantages */
.advantages{top:1008px;height:475px;color:var(--white);text-align:center}
.adv-photo{position:absolute;inset:0;background:linear-gradient(180deg,#47665f 0%,#4f736b 50%,#3f5f58 100%)}
.band-title{position:absolute;left:0;width:1200px;font-family:"Roboto Slab",Georgia,serif;font-size:29px;font-weight:500}
.band-rule{position:absolute;left:505px;width:190px;height:2px;background:var(--white)}
.adv-item{position:absolute;top:152px;width:190px}
.adv-item svg{display:block;margin:0 auto}
.adv-item h3{font-family:"Roboto",Arial,sans-serif;font-weight:500;font-size:19px;margin-top:24px}
.adv-item p{font-size:12px;line-height:19px;margin-top:14px}
.side-arrow{position:absolute}

/* how it works */
.how{top:1483px;height:510px;background:var(--mist);text-align:center}
.how-intro{position:absolute;left:200px;width:800px;top:95px;font-family:"Raleway",Arial,sans-serif;font-size:13.5px;line-height:24px;color:#555}
.step{position:absolute;top:194px;width:240px}
.step h3{font-family:"Roboto",Arial,sans-serif;font-weight:500;font-size:17px;color:var(--rust);margin-top:26px;letter-spacing:.3px}
.step.alt h3{color:var(--teal)}
.step p{font-family:"Raleway",Arial,sans-serif;font-size:12px;line-height:21px;color:#666;margin:14px auto 0;width:225px}

/* testimonial */
.quote{top:1993px;height:370px;color:var(--white);text-align:center}
.quote-photo{position:absolute;inset:0;background:linear-gradient(180deg,#4d5c3e 0%,#485839 100%)}
.quote-mark{position:absolute;font-family:"Roboto Slab",Georgia,serif;font-size:90px;line-height:1}
.quote-text{position:absolute;left:150px;width:900px;top:137px;font-family:"Roboto",Arial,sans-serif;font-weight:500;font-size:15.5px;line-height:31px}
.dots{position:absolute;top:2299px;left:548px;display:flex;gap:8px}
.dots i{width:15px;height:15px;border:1.5px solid var(--white);border-radius:50%;display:block}
.dots i.on{background:var(--rust)}

/* footer */
.site-footer{top:2363px;height:410px;background:var(--footer);color:var(--white)}
.foot-brand{position:absolute;left:98px;top:105px;width:220px;text-align:center}
.foot-col{position:absolute;top:52px}
.foot-col h4{font-family:"Roboto",Arial,sans-serif;font-weight:500;font-size:17px;padding-bottom:12px;border-bottom:2px solid var(--white);display:inline-block}
.foot-links{list-style:none;margin-top:18px;font-family:"Raleway",Arial,sans-serif;font-size:14px;color:var(--gold)}
.foot-links li{margin-bottom:14px}
.contact-row{display:flex;gap:20px;margin-top:20px;font-size:12.5px;line-height:20px}
.contact-row b{font-family:"Roboto",Arial,sans-serif;font-weight:700;font-size:14px;display:block}
.pin{width:38px;height:38px;border:1.5px solid var(--gold);border-radius:50%;flex:none;display:flex;align-items:center;justify-content:center}
.field{position:absolute;border:1px solid #ddd;border-radius:3px;font-size:11px;padding:8px 10px;color:var(--white);font-family:"Raleway",Arial,sans-serif}
.send{position:absolute;background:var(--gold);color:var(--footer);font-size:11px;font-family:"Roboto",Arial,sans-serif;padding:10px 14px;border-radius:2px}
.foot-rule{position:absolute;left:98px;top:340px;width:1004px;height:1px;background:#6a5a5c}
.copyright{position:absolute;left:98px;top:367px;font-family:"Raleway",Arial,sans-serif;font-size:13.5px}
.socials{position:absolute;right:98px;top:357px;display:flex;gap:8px}
.socials i{width:33px;height:33px;border:1.5px solid var(--white);border-radius:50%;display:block}
</style>
</head>
<body>

<section class="hero">
  <div class="hero-photo" role="img" aria-label="Photo of a glass cup of Darjeeling tea on burlap in front of terraced tea gardens at sunset"></div>
  <div class="brand">
    <div class="brand-mark"></div>
    <div class="brand-name">HILLMIST TEAS</div>
  </div>
  <div class="topbar">
    <span><i class="ico-ring"><svg width="16" height="12" viewBox="0 0 16 12"><rect x="1" y="1" width="14" height="10" fill="none" stroke="#b6482a" stroke-width="1.5"/><path d="M1 1l7 6 7-6" fill="none" stroke="#b6482a" stroke-width="1.5"/></svg></i>Info@hillmistteas.in</span>
    <span><i class="ico-ring" style="background:none;border:2px solid #fff"><svg width="14" height="14" viewBox="0 0 14 14"><path d="M3 1l2 3-1.5 1.5a8 8 0 0 0 5 5L10 9l3 2-1.5 2.5C6 13 1 8 .5 2.5z" fill="#fff"/></svg></i>+1800 4141 7272</span>
    <span><svg width="26" height="30" viewBox="0 0 26 30"><path d="M8 9V6a5 5 0 0 1 10 0v3" fill="none" stroke="#fff" stroke-width="2"/><rect x="2" y="9" width="22" height="20" fill="#fff"/></svg>0 CART: £0.00</span>
  </div>
  <nav class="nav">
    <a class="current">HOME</a><a>SHOP</a><a>DARJEELING</a><a>PURE &amp; ORGANIC</a><a>ABOUT US</a><a>CONTACT US</a>
  </nav>
  <h1 class="hero-title">Organic Darjeeling Tea</h1>
  <p class="hero-sub">Tried of paying outrageous prices for darjeeling tea?<br>we fixed that for you.</p>
  <div class="hero-arrows">
    <span class="round-btn"><svg width="12" height="16" viewBox="0 0 12 16"><path d="M9 2L3 8l6 6" fill="none" stroke="#fff" stroke-width="2"/></svg></span>
    <span class="round-btn"><svg width="12" height="16" viewBox="0 0 12 16"><path d="M3 2l6 6-6 6" fill="none" stroke="#fff" stroke-width="2"/></svg></span>
  </div>
</section>

<section class="teas">
  <div class="teas-photo" role="img" aria-label="Glass cup of amber Darjeeling tea beside loose black leaves, green tea leaves and a wooden scoop"></div>
  <div class="teas-body">
    <h2 class="sec-title">OUR <em>DARJEELING TEAS</em></h2>
    <p class="teas-lead">Looking for the world's most renowned tea at unbeatable low prices?</p>
    <p class="teas-copy">Darjeeling tea is carefully cultivated on the southern slopes of the Himalayan Mountains in the Darjeeling district in West Bengal, India. Its uniqueness is based on it special climate: intense sunshine in relatively cool climate conditions and grown on very steep slopes in extremely high altitudes. The alternate spells of rain and sunshine help to grow the tea. The typical fog further ensures the required level of moisture. This complex combination of agro-climatic conditions comes together with a meticulous manufacture and a disdain for quantity.</p>
    <span class="btn">BUY NOW</span>
  </div>
</section>

<section class="advantages">
  <div class="adv-photo" role="img" aria-label="Misty green tea plantation background"></div>
  <h2 class="band-title" style="top:44px">OUR ADVANTAGES</h2>
  <div class="band-rule" style="top:92px"></div>
  <svg class="side-arrow" style="left:30px;top:205px" width="24" height="44" viewBox="0 0 24 44"><path d="M20 2L4 22l16 20" fill="none" stroke="#fff" stroke-width="2"/></svg>
  <svg class="side-arrow" style="left:1138px;top:205px" width="24" height="44" viewBox="0 0 24 44"><path d="M4 2l16 20L4 42" fill="none" stroke="#fff" stroke-width="2"/></svg>

  <div class="adv-item" style="left:90px">
    <svg width="150" height="160" viewBox="0 0 150 160"><path d="M75 150l-14-13a68 68 0 1 1 28 0z" fill="#fff"/><path d="M60 70h10l10-22c6 0 8 4 6 12l-3 10h15c5 0 7 4 5 8l-6 22c-1 4-4 6-8 6H60z" fill="#3b5956"/><rect x="46" y="70" width="11" height="36" fill="#3b5956"/></svg>
    <h3>Highest Quality</h3><p>We ensure you get First and Second Flush Teas with the highest leaf gradation.</p>
  </div>
  <div class="adv-item" style="left:299px">
    <svg width="150" height="160" viewBox="0 0 150 160"><path d="M75 150l-14-13a68 68 0 1 1 28 0z" fill="#fff"/><circle cx="75" cy="76" r="62" fill="#353a3a"/><path d="M75 104c-18-10-22-30-6-46 4 16 10 26 6 46zM75 104c18-10 22-30 6-46-4 16-10 26-6 46zM75 104c-8-8-24-8-32-2 10 8 22 8 32 2zM75 104c8-8 24-8 32-2-10 8-22 8-32 2z" fill="#fff"/></svg>
    <h3>100% Organic</h3><p>All our tea is from certified organic production. Inspected by internationally.</p>
  </div>
  <div class="adv-item" style="left:508px">
    <svg width="150" height="160" viewBox="0 0 150 160"><path d="M75 150l-14-13a68 68 0 1 1 28 0z" fill="#fff"/><rect x="45" y="54" width="60" height="40" fill="none" stroke="#3b5956" stroke-width="4"/><path d="M55 74h5M62 66v16M68 62v24M74 68v12M80 64v20M86 70v8M92 66v16" stroke="#3b5956" stroke-width="3"/><path d="M68 94v8h14v-8M60 104h30" stroke="#3b5956" stroke-width="4" fill="none"/></svg>
    <h3>Full Transparency</h3><p>Look up pesticide analysis results of your tea and find out from which Darjeeling.</p>
  </div>
  <div class="adv-item" style="left:717px">
    <svg width="150" height="160" viewBox="0 0 150 160"><path d="M75 150l-14-13a68 68 0 1 1 28 0z" fill="#fff"/><path d="M75 44l7 6 9-2 3 9 9 3-2 9 6 7-6 7 2 9-9 3-3 9-9-2-7 6-7-6-9 2-3-9-9-3 2-9-6-7 6-7-2-9 9-3 3-9 9 2z" fill="none" stroke="#3b5956" stroke-width="4"/><text x="75" y="88" text-anchor="middle" font-family="Roboto,Arial,sans-serif" font-size="32" font-weight="700" fill="#3b5956">$</text></svg>
    <h3>Low Price</h3><p>We did everything to eliminate all unnecessary costs in order to provide you the low.</p>
  </div>
  <div class="adv-item" style="left:916px;width:210px">
    <svg width="150" height="160" viewBox="0 0 150 160"><path d="M75 150l-14-13a68 68 0 1 1 28 0z" fill="#fff"/><ellipse cx="75" cy="98" rx="34" ry="7" fill="none" stroke="#3b5956" stroke-width="4"/><path d="M50 66h44c0 16-8 28-22 28s-22-12-22-28z" fill="none" stroke="#3b5956" stroke-width="4"/><path d="M94 70c10 0 10 12 0 12" fill="none" stroke="#3b5956" stroke-width="4"/><ellipse cx="72" cy="66" rx="22" ry="5" fill="none" stroke="#3b5956" stroke-width="3"/></svg>
    <h3>Hand-Picked Reserve</h3><p style="width:190px;margin-left:auto;margin-right:auto">We did everything to eliminate all unnecessary costs in order to provide you the low.</p>
  </div>
</section>

<section class="how">
  <h2 class="sec-title" style="position:absolute;top:36px;left:0;width:1200px;font-size:29px">HOW <em>IT WORKS</em></h2>
  <p class="how-intro">How can it be that we offer you one of the world's most sought after teas for an unbeatable low price? Your main benefits if you order at Hillmist Teas:</p>

  <svg class="abs" style="left:0;top:150px" width="1200" height="130" viewBox="0 0 1200 130">
    <path d="M290 44q40-30 80 0" fill="none" stroke="#3b5956" stroke-width="3"/><path d="M362 34l10 12-14 2" fill="none" stroke="#3b5956" stroke-width="3"/>
    <path d="M555 120q40 30 80-10" fill="none" stroke="#3b5956" stroke-width="3"/><path d="M624 106l12 2-4 13" fill="none" stroke="#3b5956" stroke-width="3"/>
    <path d="M818 44q40-30 80 0" fill="none" stroke="#3b5956" stroke-width="3"/><path d="M890 34l10 12-14 2" fill="none" stroke="#3b5956" stroke-width="3"/>
  </svg>

  <div class="step" style="left:74px">
    <svg width="160" height="150" viewBox="0 0 160 150"><circle cx="80" cy="80" r="64" fill="#fff" stroke="#b6482a" stroke-width="3"/><circle cx="80" cy="80" r="57" fill="#b6482a"/><path d="M60 66l20-10 20 10v26l-20 10-20-10z M60 66l20 10 20-10 M80 76v26" fill="none" stroke="#fff" stroke-width="3.5"/><circle cx="130" cy="28" r="20" fill="#3b5956"/><text x="130" y="35" text-anchor="middle" font-family="Roboto,Arial,sans-serif" font-size="19" fill="#fff">1</text></svg>
    <h3>LARGE PACKAGES</h3><p>By using large packets (500g, 1000g), we can save on packaging, labeling and handling costs.</p>
  </div>
  <div class="step" style="left:331px">
    <svg width="160" height="150" viewBox="0 0 160 150"><circle cx="80" cy="80" r="64" fill="#fff" stroke="#b6482a" stroke-width="3"/><circle cx="80" cy="80" r="57" fill="#b6482a"/><rect x="58" y="60" width="44" height="32" fill="none" stroke="#fff" stroke-width="3.5"/><path d="M64 84l10-10 8 6 12-14M72 100h16M80 92v8" fill="none" stroke="#fff" stroke-width="3.5"/><circle cx="130" cy="28" r="20" fill="#3b5956"/><text x="130" y="35" text-anchor="middle" font-family="Roboto,Arial,sans-serif" font-size="19" fill="#fff">2</text></svg>
    <h3>DIRECT TRADE</h3><p>We cut all middlemen and buy directly from the leaf meadows in Darjeeling.</p>
  </div>
  <div class="step alt" style="left:597px">
    <svg width="160" height="150" viewBox="0 0 160 150"><circle cx="80" cy="80" r="64" fill="#fff" stroke="#3b5956" stroke-width="3"/><circle cx="80" cy="80" r="57" fill="#3b5956"/><ellipse cx="70" cy="72" rx="9" ry="13" transform="rotate(-30 70 72)" fill="#fff"/><ellipse cx="92" cy="74" rx="9" ry="13" transform="rotate(30 92 74)" fill="#fff"/><ellipse cx="80" cy="94" rx="9" ry="13" transform="rotate(90 80 94)" fill="#fff"/><circle cx="130" cy="28" r="20" fill="#b6482a"/><text x="130" y="35" text-anchor="middle" font-family="Roboto,Arial,sans-serif" font-size="19" fill="#fff">3</text></svg>
    <h3>SIMPLICITY</h3><p>We only sell 100% organic high grad FTGFOP-1 darjeeling tea to reduce costs. Nothing else</p>
  </div>
  <div class="step" style="left:854px">
    <svg width="160" height="150" viewBox="0 0 160 150"><circle cx="80" cy="80" r="64" fill="#fff" stroke="#b6482a" stroke-width="3"/><circle cx="80" cy="80" r="57" fill="#b6482a"/><rect x="54" y="64" width="32" height="26" fill="#fff"/><path d="M86 72h12l8 10v8H86z" fill="#fff"/><circle cx="64" cy="94" r="6" fill="#fff" stroke="#b6482a" stroke-width="2"/><circle cx="98" cy="94" r="6" fill="#fff" stroke="#b6482a" stroke-width="2"/><path d="M70 70v14M63 77h14" stroke="#b6482a" stroke-width="3"/><circle cx="130" cy="28" r="20" fill="#3b5956"/><text x="130" y="35" text-anchor="middle" font-family="Roboto,Arial,sans-serif" font-size="19" fill="#fff">4</text></svg>
    <h3>ONE YEAR'S SUPPLY</h3><p>Tea stores well for long periods of time. Therefore many of our customers buy their year's supply at a time.</p>
  </div>
</section>

<section class="quote">
  <div class="quote-photo" role="img" aria-label="Dark green tea leaf background"></div>
  <span class="quote-mark" style="left:130px;top:60px">&ldquo;</span>
  <span class="quote-mark" style="left:1010px;top:222px">&rdquo;</span>
  <h2 class="band-title" style="top:62px;font-weight:700;font-size:38px">VERY GOOD TEA!</h2>
  <p class="quote-text">DARJEELING TEA is India's treasured Geographical Indication and forms a very important part of India's cultural and collective intellectual heritage. This special tea cannot be grown or manufactured anywhere else in the world. Just as Champagne is indigenous to the Champagne district of France, so is DARJEELING TEA to Darjeeling.</p>
  <svg class="side-arrow" style="left:30px;top:150px" width="24" height="44" viewBox="0 0 24 44"><path d="M20 2L4 22l16 20" fill="none" stroke="#fff" stroke-width="2"/></svg>
  <svg class="side-arrow" style="left:1138px;top:150px" width="24" height="44" viewBox="0 0 24 44"><path d="M4 2l16 20L4 42" fill="none" stroke="#fff" stroke-width="2"/></svg>
</section>
<div class="dots"><i></i><i class="on"></i><i></i><i></i><i></i></div>

<footer class="site-footer">
  <div class="foot-brand">
    <div class="brand-mark"></div>
    <div class="brand-name">HILLMIST TEAS</div>
  </div>
  <div class="foot-col" style="left:383px">
    <h4>QUICK LINKS</h4>
    <ul class="foot-links"><li>› Home</li><li>› About Us</li><li>› Advantages</li><li>› How it works</li><li>› Products</li><li>› Contact Us</li></ul>
  </div>
  <div class="foot-col" style="left:551px;width:260px">
    <h4>CONTACT US</h4>
    <div class="contact-row"><span class="pin"><svg width="12" height="16" viewBox="0 0 12 16"><path d="M6 15C2 10 1 8 1 6a5 5 0 0 1 10 0c0 2-1 4-5 9z" fill="none" stroke="#dcc17d" stroke-width="1.5"/><circle cx="6" cy="6" r="1.8" fill="#dcc17d"/></svg></span><div><b>HILLMIST TEAS,</b>42 Fernhollow Rd.<br>Kestrel Bay, NL B2K 4R7.</div></div>
    <div class="contact-row"><span class="pin"><svg width="10" height="16" viewBox="0 0 10 16"><rect x="1" y="1" width="8" height="14" rx="1.5" fill="none" stroke="#dcc17d" stroke-width="1.5"/></svg></span><div><b>PHONE:</b>1 555 010 274</div></div>
    <div class="contact-row"><span class="pin" style="background:var(--gold)"><svg width="14" height="10" viewBox="0 0 14 10"><rect x="0.5" y="0.5" width="13" height="9" fill="none" stroke="#3c2e30"/><path d="M1 1l6 5 6-5" fill="none" stroke="#3c2e30"/></svg></span><div><b>Mail:</b>info@hillmistteas.co.uk</div></div>
  </div>
  <div class="foot-col" style="left:847px">
    <h4>CONTACT FORM</h4>
  </div>
  <span class="field" style="left:847px;top:114px;width:122px;height:37px">Name</span>
  <span class="field" style="left:978px;top:114px;width:122px;height:37px">Phone</span>
  <span class="field" style="left:847px;top:160px;width:253px;height:68px">Message</span>
  <span class="send" style="left:847px;top:242px">SEND MESSAGE</span>
  <div class="foot-rule"></div>
  <p class="copyright">Copyright © 2016 Hillmist Teas. All Right Reserved</p>
  <div class="socials"><i></i><i></i><i></i><i></i></div>
</footer>

</body>
</html>
```